Dorian Walsby Psychotherapy Business Card Design Project

I need a welcoming business card for a Somatic Psychotherapy private practice based in Melbourne, Australia. I help individual clients to work through issues in their life that are inhibiting achieving their full potential. I would like a san serif font and the oculars are:
blue: R:37 G:61 B:95 C:93 M:77 Y:38 K:28
orange: R:241 G:103 B:43 C:0 M:74 Y:93 K:0
The final design should communicate warm, welcoming and safe environment in which clients are supported to grow. It should also convey a collaborative approach to achieve success between me (the therapist) and the client. The uploaded file is my new logo. Also an organic look and feel while maintaining professionalism and a clean, simple look is sought after.
In addition to the logo my details are:
Dorian Walsby
Psychotherapist
B.Arts., Grad Dip. T&D., Dip.Som.Psych, MRKTA, MLOHVB
0417 582 930
dwalsby@dorianwalsby.com.au
www.dorianwalsby.com.au
Target Market(s)
Psychotherapy Clients
Industry/Entity Type
Environment

```html
<!DOCTYPE html>
<html lang="en">
<head>
<meta charset="utf-8">
<title>Dorian Walsby Psychotherapy – Business Card</title>
<link rel="stylesheet" href="https://fonts.googleapis.com/css2?family=Open+Sans:wght@400;600;700&display=swap">
<style>
  :root {
    --blue: #253d5f;
    --orange: #f1672b;
    --ink: #1d1d1d;
    --card: #ffffff;
    --backdrop: #e7e4df;
  }
  * { box-sizing: border-box; margin: 0; padding: 0; }
  html, body {
    width: 1200px; height: 502px; overflow: hidden;
    background: var(--backdrop);
    font-family: "Open Sans", Arial, sans-serif;
  }
  .stage { position: relative; width: 1200px; height: 502px; }
  .card {
    position: absolute; top: 80px;
    width: 528px; height: 322px;
    background: var(--card);
    border-radius: 16px;
    box-shadow: 0 2px 8px rgba(0,0,0,0.12);
  }
  .card--front { left: 56px; }
  .card--back { left: 618px; }

  .brand {
    position: absolute; left: 56px; top: 70px;
    color: var(--blue); font-weight: 600;
    font-size: 34px; line-height: 1.08; letter-spacing: -0.3px;
  }

  .contact {
    position: absolute; left: 24px; right: 26px; bottom: 20px;
    display: flex; justify-content: space-between; align-items: flex-end;
  }
  .contact__name { color: var(--orange); font-weight: 700; font-size: 18px; line-height: 1.3; }
  .contact__role { color: var(--ink); font-size: 17px; line-height: 1.35; }
  .contact__creds { color: var(--ink); font-size: 10.5px; margin-top: 6px; }
  .contact__phone { color: var(--ink); font-size: 19px; margin-bottom: 28px; }
  .contact__phone b { font-weight: 700; }

  .back-name {
    position: absolute; left: 0; right: 0; top: 118px;
    text-align: center; color: var(--blue);
    font-weight: 600; font-size: 32px; line-height: 1.12;
  }
  .back-url {
    position: absolute; left: 0; right: 0; bottom: 16px;
    text-align: center; color: var(--ink);
    font-size: 13px; font-weight: 600;
  }
</style>
</head>
<body>
<main class="stage">
  <section class="card card--front">
    <p class="brand">Dorian Walsby<br>Psychotherapy</p>
    <div class="contact">
      <div class="contact__person">
        <p class="contact__name">Dorian Walsby</p>
        <p class="contact__role">Psychotherapist</p>
        <p class="contact__creds">B.Arts., Grad Dip. T&amp;D., Dip.Som.Psych, MRKTA, MLOHVB</p>
      </div>
      <p class="contact__phone"><b>Ph :</b> 0417 582 930</p>
    </div>
  </section>

  <section class="card card--back">
    <p class="back-name">Dorian Walsby<br>Psychotherapy</p>
    <p class="back-url">www.dorianwalsby.com.au</p>
  </section>
</main>
</body>
</html>
```